Banners for a bowtie/tie Fashion shop

I need banners (770x100) for a necktie and bowtie shop (http://www.kelorin.dk)

5 BOWTIE BANNERS:

I need the 3 text versions for eatch bowtie banner:

Danmarks største udvalg af butterfly
Køb butterfly. FRI fragt og FRI retur
Butterfly fra 199,- inkl. FRI fragt

5 NECKTIE BANNERS:

I need the 3 text versions for eatch necktie banner:

Danmarks største udvalg af slips
Køb slips. FRI fragt og FRI retur
Slips fra 199,- inkl. FRI fragt

All banners should contain the logo. All in JPG format and Photoshop/Inddesign/illustrator format

Target Market(s)

Guys and Gays

Industry/Entity Type

Shop

Requirements
Must have
• Logo
Nice to have
• Nice new pictures

```html
<!DOCTYPE html>
<html lang="da">
<head>
<meta charset="UTF-8">
<title>Kelorin – Danmarks største udvalg af slips</title>
<link rel="stylesheet" href="https://fonts.googleapis.com/css2?family=Cabin+Sketch:wght@400;700&display=swap">
<style>
  :root {
    --board-dark: #1f2021;
    --board-mid: #3a3b3c;
    --board-light: #4a4b4c;
    --chalk: #f2f2f0;
    --chalk-blue: #2b8fe6;
    --corner: #ffffff;
    --brand-ink: #2e2e2e;
    --suit: #2a2c30;
    --shirt: #cfd6de;
  }
  * { margin: 0; padding: 0; box-sizing: border-box; }
  html, body {
    width: 1200px;
    height: 156px;
    overflow: hidden;
    background: var(--board-dark);
  }
  .banner {
    display: block;
    position: relative;
    width: 1200px;
    height: 156px;
    overflow: hidden;
    text-decoration: none;
    background:
      radial-gradient(ellipse 55% 90% at 50% 45%, var(--board-light) 0%, var(--board-mid) 45%, var(--board-dark) 100%);
  }
  .board-lines {
    position: absolute;
    left: 0;
    top: 0;
    width: 1200px;
    height: 156px;
  }
  .model-photo {
    position: absolute;
    left: 0;
    top: 0;
    width: 262px;
    height: 156px;
    background: linear-gradient(90deg, var(--shirt) 0%, var(--suit) 35%, var(--suit) 75%, rgba(42,44,48,0) 100%);
  }
  .headline {
    position: absolute;
    left: 0;
    top: 26px;
    width: 1208px;
    text-align: center;
    white-space: nowrap;
    font-family: "Cabin Sketch", cursive;
    font-weight: 700;
    font-size: 60px;
    line-height: 48px;
    letter-spacing: 4px;
    color: var(--chalk);
    text-transform: uppercase;
  }
  .headline .highlight { color: var(--chalk-blue); }
  .brand-corner {
    position: absolute;
    left: 0;
    top: 0;
    width: 1200px;
    height: 156px;
  }
  .brand-name {
    position: absolute;
    right: 16px;
    bottom: 22px;
    font-family: "Cabin Sketch", cursive;
    font-weight: 700;
    font-size: 24px;
    line-height: 1;
    color: var(--brand-ink);
  }
</style>
</head>
<body>
  <a class="banner" href="http://www.kelorin.dk" aria-label="Kelorin – Danmarks største udvalg af slips">
    <svg class="board-lines" viewBox="0 0 1200 156" aria-hidden="true">
      <line x1="330" y1="156" x2="720" y2="0" stroke="rgba(255,255,255,0.18)" stroke-width="1"/>
      <line x1="560" y1="0" x2="930" y2="156" stroke="rgba(255,255,255,0.12)" stroke-width="1"/>
      <line x1="620" y1="0" x2="1080" y2="80" stroke="rgba(255,255,255,0.10)" stroke-width="1"/>
    </svg>
    <div class="model-photo" role="img" aria-label="Mand i mørkt jakkesæt med hvid skjorte og mørkt slips"></div>
    <h1 class="headline">Danmarks største<br>udvalg af <span class="highlight">slips</span></h1>
    <svg class="brand-corner" viewBox="0 0 1200 156" aria-hidden="true">
      <polygon points="950,156 1200,47 1200,156" fill="#ffffff"/>
    </svg>
    <span class="brand-name">kelorin</span>
  </a>
</body>
</html>
```